Quiet Falcon Coffee

We need a website to sell coffee with a horse theme. We already have a logo and have designed 4 different coffee bags/flavors so far, each of which will be available in ground or whole bean. The brand is intended to be light hearted/whimsical.

Coding

Coded - Design and coding required

Number of Pages Required

4 page

Requirements
Must have
• incorporation of attached photos
Nice to have
• underlying background theme with sky/grass

```html
<!DOCTYPE html>
<html lang="en">
<head>
<meta charset="utf-8">
<title>Quiet Falcon Coffee</title>
<link rel="stylesheet" href="https://fonts.googleapis.com/css2?family=Marcellus&family=Cormorant+Garamond:wght@500&family=Poppins:ital,wght@0,400;0,500;0,600;1,400&display=swap">
<style>
:root{
  --brown:#3b2616;
  --brown-deep:#2f1e11;
  --cream:#fdf3ea;
  --bag-cream:#fcefdc;
  --label:#dba97a;
  --paper:#f2f2f2;
  --text:#2a2a2a;
  --line:#3b2616;
  --white:#ffffff;
  --tan:#c9a27a;
}
*{box-sizing:border-box;margin:0;padding:0}
html,body{width:1200px;height:5195px;overflow:hidden}
body{position:relative;font-family:"Poppins",sans-serif;color:var(--text);background:var(--white)}
.abs{position:absolute}
.heading{font-family:"Marcellus",serif;color:var(--brown-deep);font-weight:400;text-align:center;letter-spacing:1px}
.divider{display:flex;align-items:center;justify-content:center;gap:8px}
.divider span{display:block;width:40px;height:2px;background:var(--line)}
.divider i{display:block;width:14px;height:12px;position:relative}
.divider i::before,.divider i::after{content:"";position:absolute;width:6px;height:6px;border-radius:50%;background:var(--brown)}
.divider i::before{left:0;top:5px;box-shadow:8px 0 0 var(--brown)}
.divider i::after{left:4px;top:0}
.btn{position:absolute;display:flex;align-items:center;justify-content:center;border-radius:30px;font-size:15px}
.btn-dark{background:var(--brown);color:var(--white)}
.btn-outline{border:2px solid var(--brown);color:var(--brown)}

/* header */
.site-header{left:0;top:0;width:1200px;height:152px;background:var(--white)}
.brand{left:62px;top:50px;display:flex;align-items:center;gap:10px;font-family:"Marcellus",serif;font-size:21px;color:var(--brown);line-height:1.1}
.brand .mark{width:26px;height:26px;border-radius:50%;background:var(--brown)}
.search{left:876px;top:40px;width:174px;height:32px;border:2px solid var(--brown);border-radius:16px;font-size:12px;color:#999;padding:6px 18px}
.nav{left:650px;top:100px;display:flex;gap:38px;font-size:13.5px;color:var(--text)}
.nav .active{border-bottom:2px solid var(--brown);padding-bottom:6px}

/* hero */
.hero{left:0;top:152px;width:1200px;height:556px;background:linear-gradient(100deg,#cfcdcc 0%,#b9b7b5 55%,#8a7766 80%,#5a3a25 100%)}
.hero-panel{left:78px;top:215px;width:710px;height:433px;border-radius:90px;background:rgba(243,242,240,.95)}
.hero-title{left:78px;top:268px;width:710px;font-size:82px;line-height:90px}
.hero-copy{left:130px;top:462px;width:606px;text-align:center;font-size:13px;line-height:17px;color:var(--text)}

/* products */
.products{left:0;top:708px;width:1200px;height:760px;background:var(--cream)}
.bag{width:247px;height:410px;top:893px;border:2px solid var(--brown);background:linear-gradient(var(--bag-cream) 0 67%,var(--brown) 67% 100%);overflow:hidden}
.bag-art{position:absolute;left:48px;top:8px;width:148px;height:160px;border-radius:40%;background:radial-gradient(ellipse at 50% 50%,#b98a62 0%,#d9b896 45%,var(--bag-cream) 72%)}
.bag-brand{position:absolute;left:0;top:172px;width:100%;text-align:center;font-family:"Marcellus",serif;color:var(--brown-deep);font-size:27px;line-height:30px}
.bag-brand small{display:block;font-size:15px;letter-spacing:5px;line-height:22px}
.bag-label{position:absolute;left:32px;top:248px;width:180px;height:150px;background:var(--label);color:var(--brown-deep);text-align:center;padding-top:8px}
.bag-name{font-size:11.5px;font-weight:600;letter-spacing:.5px;line-height:16px}
.bag-row{display:flex;justify-content:center;align-items:center;gap:6px;margin-top:5px;font-size:6.5px;font-weight:600;line-height:8px}
.bag-row .roast{border-right:1px solid var(--brown-deep);padding-right:6px}
.bag-dist{margin-top:8px;font-size:7px;font-weight:600;line-height:9px;letter-spacing:.4px}
.bag-site{margin-top:9px;font-size:6.5px;font-weight:600;letter-spacing:.4px}
.bag-weight{margin-top:5px;font-size:7px;font-weight:600;letter-spacing:.4px}

/* about */
.about-copy{left:578px;top:1636px;width:509px;font-size:13.5px;line-height:24px;text-align:justify;color:#333}

/* features */
.features{left:0;top:2038px;width:1200px;height:365px;background:var(--brown)}
.feature-box{width:180px;height:180px;top:2107px;border:2px solid var(--tan);display:flex;align-items:center;justify-content:center}
.feature-label{top:2297px;width:180px;text-align:center;color:var(--white);font-size:18px;line-height:22px}

/* promo */
.promo{left:0;top:2403px;width:1200px;height:602px;background:linear-gradient(90deg,#e2e1df,#d4d1cd 70%,#b9aa9a)}
.promo-photo{left:0;top:2403px;width:563px;height:602px;border-radius:0 120px 0 0;background:radial-gradient(ellipse at 45% 55%,#e6e2de 0%,#8b7e74 25%,#3a2b22 55%,#140d09 100%)}
.promo-title{left:580px;top:2512px;width:565px;font-family:"Cormorant Garamond",serif;font-weight:500;font-size:72px;line-height:74px;text-align:center;color:var(--brown-deep)}

/* testimonials */
.testimonial-card{left:198px;top:3195px;width:805px;height:473px;border:3px solid var(--brown);border-radius:12px;background:var(--white)}
.arrow{width:38px;height:38px;border:2px solid #bbb;border-radius:8px;display:flex;align-items:center;justify-content:center;top:3396px}

/* newsletter */
.newsletter{left:0;top:3795px;width:1200px;height:340px;background:linear-gradient(90deg,#bdbcba,#d9d7d4 50%,#bcbab7)}
.email{left:147px;top:4004px;width:708px;height:51px;background:var(--white);font-size:16px;color:#777;padding:14px 22px}
.email-submit{left:855px;top:4004px;width:173px;height:51px;background:var(--brown-deep);color:var(--white);font-size:16px;display:flex;align-items:center;justify-content:center}

/* contact */
.contact{left:0;top:4135px;width:1200px;height:625px;background:var(--paper)}
.contact-photo{left:152px;top:4375px;width:330px;height:328px;border-radius:14px;background:radial-gradient(ellipse at 40% 45%,#f4efe8 0%,#d89a62 30%,#9b4d1f 65%,#5c2a10 100%)}
.field{background:var(--white);border:1px solid #e3e3e3;font-size:12px;color:#aaa;padding:14px 12px}

/* footer */
.footer-title{font-family:"Marcellus",serif;font-size:26px;color:var(--brown-deep);font-weight:400}
.footer-list{list-style:none;font-size:14.5px;line-height:32.5px}
.footer-list li::before{content:"";display:inline-block;width:7px;height:7px;border-radius:50%;background:#222;margin-right:14px;vertical-align:middle}
.social{width:36px;height:36px;border-radius:50%;background:var(--brown-deep);top:5027px}
.contact-item{left:810px;display:flex;gap:14px;font-size:15px;line-height:24px;color:#222}
.contact-icon{width:34px;height:34px;border-radius:50%;background:var(--brown-deep);display:flex;align-items:center;justify-content:center;flex:none}
</style>
</head>
<body>

<header class="abs site-header">
  <div class="abs brand"><span class="mark"></span><span>Quiet Falcon<br>Coffee</span></div>
  <div class="abs search">Search</div>
  <svg class="abs" style="left:1062px;top:40px" width="34" height="30" viewBox="0 0 34 30" fill="none" stroke="#3b2616" stroke-width="2"><path d="M2 4h5l4 16h16l3-11H9"/><circle cx="13" cy="25" r="2"/><circle cx="25" cy="25" r="2"/></svg>
  <svg class="abs" style="left:1108px;top:40px" width="28" height="28" viewBox="0 0 28 28" fill="#111"><circle cx="14" cy="9" r="6"/><path d="M3 26c0-7 5-10 11-10s11 3 11 10z"/></svg>
  <nav class="abs nav"><span class="active">Home</span><span>Our Product</span><span>About Us</span><span>Testimonials</span><span>Contact Us</span></nav>
</header>

<section class="abs hero" role="img" aria-label="Coffee cup on a saucer surrounded by roasted coffee beans on a grey stone surface"></section>
<div class="abs hero-panel"></div>
<h1 class="abs heading hero-title">START A DAY<br>WITH COFFEE</h1>
<p class="abs hero-copy">Lorem ipsum dolor sit amet, consectetur adipiscing elit, sed do eiusmod tempor incididunt ut labore et dolore magna aliqua.</p>
<div class="btn btn-dark" style="left:200px;top:528px;width:223px;height:48px">Shop Here</div>
<div class="btn btn-outline" style="left:443px;top:528px;width:221px;height:48px">View Our Product</div>

<section class="abs products"></section>
<h2 class="abs heading" style="left:0;top:775px;width:1200px;font-size:46px">OUR PRODUCT</h2>
<div class="abs divider" style="left:0;top:836px;width:1200px"><span></span><i></i><span></span></div>

<article class="abs bag" style="left:68px">
  <div class="bag-art" role="img" aria-label="Illustrated rider on a bucking horse"></div>
  <div class="bag-brand">Quiet Falcon<small>COFFEE</small></div>
  <div class="bag-label">
    <div class="bag-name">• SADDLE UP •</div>
    <div class="bag-row"><span class="roast">MEDIUM ROAST</span><span>WHOLE BEAN COFFEE<br>GROUND COFFEE</span></div>
    <div class="bag-dist">DISTRIBUTED BY<br>QUIET FALCON COFFEE<br>MAPLETON · ST · 00000</div>
    <div class="bag-site">QUIETFALCON COFFEE</div>
    <div class="bag-weight">NET WT 12oz / 340g</div>
  </div>
</article>
<article class="abs bag" style="left:342px">
  <div class="bag-art" role="img" aria-label="Illustrated rider on a prancing horse"></div>
  <div class="bag-brand">Quiet Falcon<small>COFFEE</small></div>
  <div class="bag-label">
    <div class="bag-name">• HIGH STEPPER •</div>
    <div class="bag-row"><span class="roast">DARK ROAST</span><span>WHOLE BEAN COFFEE<br>GROUND COFFEE</span></div>
    <div class="bag-dist">DISTRIBUTED BY<br>QUIET FALCON COFFEE<br>MAPLETON · ST · 00000</div>
    <div class="bag-site">QUIETFALCON COFFEE</div>
    <div class="bag-weight">NET WT 12oz / 340g</div>
  </div>
</article>
<article class="abs bag" style="left:615px">
  <div class="bag-art" role="img" aria-label="Illustrated rider jumping a fence"></div>
  <div class="bag-brand">Quiet Falcon<small>COFFEE</small></div>
  <div class="bag-label">
    <div class="bag-name">• FENCE JUMPER BLEND •</div>
    <div class="bag-row"><span class="roast">CARAMEL<br>CREAM</span><span>WHOLE BEAN COFFEE<br>GROUND COFFEE</span></div>
    <div class="bag-dist">DISTRIBUTED BY<br>QUIET FALCON COFFEE<br>MAPLETON · ST · 00000</div>
    <div class="bag-site">QUIETFALCON COFFEE</div>
    <div class="bag-weight">NET WT 12oz / 340g</div>
  </div>
</article>
<article class="abs bag" style="left:889px">
  <div class="bag-art" role="img" aria-label="Illustrated rider turning a barrel"></div>
  <div class="bag-brand">Quiet Falcon<small>COFFEE</small></div>
  <div class="bag-label">
    <div class="bag-name">• BARREL RACER •</div>
    <div class="bag-row"><span class="roast">LIGHT ROAST</span><span>WHOLE BEAN COFFEE<br>GROUND COFFEE</span></div>
    <div class="bag-dist">DISTRIBUTED BY<br>QUIET FALCON COFFEE<br>MAPLETON · ST · 00000</div>
    <div class="bag-site">QUIETFALCON COFFEE</div>
    <div class="bag-weight">NET WT 12oz / 340g</div>
  </div>
</article>
<div class="btn btn-dark" style="left:538px;top:1348px;width:124px;height:42px;font-size:13px">Shop Now</div>

<div class="abs" style="left:105px;top:1575px;width:423px;height:355px;border-radius:50% 45% 50% 48%;background:radial-gradient(ellipse at 50% 55%,#e8cfae 0%,#a56a3c 35%,#3a2314 75%,#1d120a 100%)" role="img" aria-label="Latte art cups framed within a coffee bean shape"></div>
<h2 class="abs heading" style="left:578px;top:1543px;font-size:46px;text-align:left">ABOUT US</h2>
<div class="abs divider" style="left:578px;top:1600px;justify-content:flex-start"><i></i><span></span></div>
<p class="abs about-copy">There are many variations of passages of Lorem Ipsum available, but the majority have suffered alteration in some form, by injected humour, or randomised words which don't look even slightly believable. If you are going to use a passage of Lorem Ipsum, you need to be sure there isn't anything embarrassing hidden in the middle of text. All the Lorem Ipsum generators on the Internet tend to repeat predefined chunks as necessary, making this the first true generator on the Internet. It uses a dictionary of over 200 Latin words, combined with a handful of model sentence structures, to generate Lorem Ipsum which looks reasonable. The generated Lorem Ipsum is therefore always free from repetition, injected humour, or non-characteristic words etc.</p>
<div class="btn btn-dark" style="left:580px;top:1913px;width:140px;height:42px;font-size:13px">Read More</div>

<section class="abs features"></section>
<div class="abs feature-box" style="left:128px"><svg width="100" height="100" viewBox="0 0 100 100" fill="none" stroke="#c9a27a" stroke-width="3"><path d="M22 48h48v10c0 14-10 22-24 22S22 72 22 58z"/><path d="M70 52c10 0 12 12 0 14"/><path d="M14 84h68"/><path d="M44 40c-6-8 6-12 0-22M54 40c-6-8 6-12 0-22"/></svg></div>
<div class="abs feature-box" style="left:506px"><svg width="100" height="110" viewBox="0 0 100 110" fill="none" stroke="#c9a27a" stroke-width="3"><rect x="18" y="10" width="64" height="92" rx="6"/><rect x="30" y="22" width="40" height="16"/><path d="M18 48h64M34 48v10h32V48"/><path d="M30 74h40v8c0 8-6 12-20 12s-20-4-20-12z"/><path d="M24 96h52"/></svg></div>
<div class="abs feature-box" style="left:885px"><svg width="100" height="100" viewBox="0 0 100 100" fill="none" stroke="#c9a27a" stroke-width="3"><path d="M12 48 50 16l38 32M22 40v44h56V40M68 24v-8h8v16"/><path d="M50 72 38 60a7 7 0 0 1 12-8 7 7 0 0 1 12 8z"/></svg></div>
<div class="abs feature-label" style="left:128px">Crafting<br>Perfection</div>
<div class="abs feature-label" style="left:506px">Beans to<br>Brews</div>
<div class="abs feature-label" style="left:885px">Cosy<br>Atmosphere</div>

<section class="abs promo" role="img" aria-label="Blurred coffee beans on a pale surface"></section>
<div class="abs promo-photo" role="img" aria-label="Steaming cup of coffee on a saucer with scattered beans on a dark table"></div>
<h2 class="abs promo-title">The best coffee<br>bean for every cup<br>of your coffee</h2>
<div class="btn btn-dark" style="left:722px;top:2790px;width:266px;height:72px;font-size:29px;border-radius:40px">Buy Now</div>

<h2 class="abs heading" style="left:0;top:3067px;width:1200px;font-size:46px">TESTIMONIALS</h2>
<div class="abs divider" style="left:0;top:3128px;width:1200px"><span></span><i></i><span></span></div>
<div class="abs testimonial-card"></div>
<div class="abs" style="left:540px;top:3240px;width:120px;height:120px;border-radius:50%;border:2px solid var(--brown);background:linear-gradient(#e9e9e9,#9a9a9a)" role="img" aria-label="Customer portrait"></div>
<p class="abs" style="left:198px;top:3388px;width:805px;text-align:center;font-style:italic;font-size:17px;color:var(--brown-deep)">DANIEL MOREAU</p>
<p class="abs" style="left:198px;top:3415px;width:805px;text-align:center;font-size:15px;color:#333">Lorem Ipsum</p>
<p class="abs" style="left:270px;top:3470px;width:660px;text-align:center;font-size:13px;line-height:22.5px;color:#333">Lorem ipsum dolor sit amet, consectetur adipiscing elit, sed do eiusmod tempor incididunt ut labore et dolore magna aliqua. Ut enim ad minim veniam, quis nostrud exercitation ullamco laboris nisi ut aliquip ex ea commodo consequat. Duis aute irure dolor in reprehenderit in voluptate velit esse cillum dolore eu fugiat nulla pariatur. Excepteur sint occaecat cupidatat non proident, sunt in culpa qui officia deserunt mollit anim id est laborum.</p>
<div class="abs arrow" style="left:127px"><svg width="16" height="16" viewBox="0 0 16 16" fill="none" stroke="#bbb" stroke-width="2.5"><path d="M11 2 5 8l6 6"/></svg></div>
<div class="abs arrow" style="left:1034px;border-color:var(--brown)"><svg width="16" height="16" viewBox="0 0 16 16" fill="none" stroke="#3b2616" stroke-width="2.5"><path d="m5 2 6 6-6 6"/></svg></div>

<section class="abs newsletter" role="img" aria-label="Coffee cup on a pale wooden table, softly blurred"></section>
<h2 class="abs heading" style="left:0;top:3850px;width:1200px;font-size:46px;color:#1a1a1a">SUBSCRIBE TO OUR NEWSLETTER</h2>
<p class="abs" style="left:0;top:3933px;width:1200px;text-align:center;font-size:19px;color:#222">Be the first to know about new products and exclusive offers.</p>
<div class="abs email">Enter a valid email address</div>
<div class="abs email-submit">SUBMIT</div>

<section class="abs contact"></section>
<h2 class="abs heading" style="left:0;top:4212px;width:1200px;font-size:46px">CONTACT US</h2>
<div class="abs divider" style="left:0;top:4273px;width:1200px"><span></span><i></i><span></span></div>
<p class="abs" style="left:0;top:4325px;width:1200px;text-align:center;font-size:15px;color:#333">For more information,Please fill out the following and we will be in touch shortly</p>
<div class="abs contact-photo" role="img" aria-label="White coffee cup with beans on a warm wooden table"></div>
<div class="abs field" style="left:612px;top:4392px;width:216px;height:48px">First Name</div>
<div class="abs field" style="left:853px;top:4392px;width:215px;height:48px">Second Name</div>
<div class="abs field" style="left:612px;top:4470px;width:216px;height:48px">Phone</div>
<div class="abs field" style="left:853px;top:4470px;width:215px;height:48px">Subject</div>
<div class="abs field" style="left:612px;top:4545px;width:460px;height:96px;padding-top:38px">Message</div>
<div class="btn btn-dark" style="left:612px;top:4673px;width:91px;height:30px;font-size:13px">Submit</div>

<footer>
  <div class="abs brand" style="left:170px;top:4915px;flex-direction:column;text-align:center;gap:8px"><span class="mark"></span><span>Quiet Falcon<br>Coffee</span></div>
  <div class="abs social" style="left:182px"></div>
  <div class="abs social" style="left:230px"></div>
  <div class="abs social" style="left:278px"></div>
  <h3 class="abs footer-title" style="left:505px;top:4848px">LINKS</h3>
  <ul class="abs footer-list" style="left:505px;top:4924px"><li>Our products</li><li>About Us</li><li>Testimonials</li><li>Contact Us</li></ul>
  <h3 class="abs footer-title" style="left:810px;top:4848px">CONTACT US</h3>
  <div class="abs contact-item" style="top:4926px"><span class="contact-icon"><svg width="16" height="18" viewBox="0 0 16 18" fill="#fff"><path d="M8 0a6 6 0 0 1 6 6c0 5-6 12-6 12S2 11 2 6a6 6 0 0 1 6-6zm0 3.5a2.5 2.5 0 1 0 0 5 2.5 2.5 0 0 0 0-5z"/></svg></span><span>465, Lorem Ipsum<br>Lorem Ipsum , Lorem Ipsum</span></div>
  <div class="abs contact-item" style="top:4998px;align-items:center"><span class="contact-icon"><svg width="16" height="16" viewBox="0 0 16 16" fill="#fff"><path d="M3 1h3l1.5 4-2 1.2a9 9 0 0 0 4.3 4.3L11 8.5l4 1.5v3a2 2 0 0 1-2 2A13 13 0 0 1 1 3a2 2 0 0 1 2-2z"/></svg></span><span>+1 555 014 2290</span></div>
  <div class="abs contact-item" style="top:5050px;align-items:center"><span class="contact-icon"><svg width="16" height="12" viewBox="0 0 16 12" fill="none" stroke="#fff" stroke-width="1.6"><rect x="1" y="1" width="14" height="10"/><path d="m1 1 7 6 7-6"/></svg></span><span>hello@quietfalcon.example</span></div>
  <div class="abs" style="left:68px;top:5123px;width:1067px;height:1px;background:#222"></div>
  <p class="abs" style="left:0;top:5152px;width:1200px;text-align:center;font-size:12px;color:#333">© 2025 Company Name, Inc. All Rights Reserved.</p>
</footer>

</body>
</html>
```